Business Card Design, including supply of raw art files plus a vector diagram of the flenzo logo and

We need the business card design for a company that is launching a new exciting product. The brief requires the submission of the following once the final design is chosen:

- business card layout including raw files
- a composite vector image file of the flenzo logo and tag line
- a standalone vector image file of the flenzo logo

The product will be launched as a customer engagement app.

It has 4 core modules which enables a person to do multiple things - book tours and activities, order takeaways, search for local deals and offers. A universal currency is at the heart of this product. When you use the app, you earn cashback rewards when shopping or buying at any of the merchant partners across the modules as . These rewards can then be used as full or part payment when buying goods or services at these merchant partners.

The business card must help us build the brand, communicate the benefit of the brand's key focus - the ability to earn and burn this universal cashback ccurrency - across the 4 modules - booking of tours and activities, ordering, searching for local deals and payment.

We would like the design to use the brand's blue colour the hex colour is: 00
Dark grey : 646464
Darker blue shadow: 058bdd
Main Blue: 0084ff

We need to translate this into a CMYK print or spot colour print.

Both print options to be supplied as separate files.

An example of the base concept we have in mind is attached for your reference.

The font used by the brand is Proxima Nova.

Industry/Entity Type

Business

Contact Information for Business Card

Carla Whitfield
Marketing
W: www.flenzo.co
M: + 61 407318265
T: +61 2 9375 4120
A: Suite 7, Level 2, 14-18 Harrow Lane, Sydney, NSW, 2000, Australia

Font styles to use
Sans Serif

Requirements
Must have
• flEnzo logo and tagline
• address details
• flEnzo icons as supplied
Nice to have
• would like to have the option of a spot varnish layer over the logo and icons at the back of the card

```html
<!DOCTYPE html>
<html lang="en">
<head>
<meta charset="utf-8">
<title>flEnzo business card – front and back</title>
<link rel="stylesheet" href="https://fonts.googleapis.com/css2?family=Source+Sans+3:wght@200;300;400;600;700&display=swap">
<style>
  :root {
    --backdrop: #3b3b3d;
    --card: #ffffff;
    --band: #daeefa;
    --brand-blue: #2e86cc;
    --brand-blue-light: #4a9fdc;
    --ink-dark: #4a4a4a;
    --ink: #5a5a5a;
    --divider: #daeefa;
  }
  * { margin: 0; padding: 0; box-sizing: border-box; }
  html, body {
    width: 1200px; height: 1200px; overflow: hidden;
    background: var(--backdrop);
    font-family: "Source Sans 3", "Myriad Pro", sans-serif;
  }
  .canvas { position: relative; width: 1200px; height: 1200px; }
  .card {
    position: absolute; left: 180px; width: 840px; height: 480px;
    background: var(--card); overflow: hidden;
  }
  .card--front { top: 96px; }
  .card--back { top: 624px; }

  .band { position: absolute; top: 0; height: 100%; background: var(--band); }
  .band--l1 { left: 38px; width: 22px; }
  .band--l2 { left: 66px; width: 18px; }
  .band--r1 { left: 757px; width: 22px; }
  .band--r2 { left: 785px; width: 18px; }

  /* Front */
  .brand-dot {
    position: absolute; left: 210px; top: 162px; width: 132px; height: 132px;
    border-radius: 50%; background: var(--brand-blue-light);
  }
  .wordmark {
    position: absolute; left: 364px; top: 150px;
    font-size: 112px; font-weight: 200; line-height: 1;
    color: var(--ink-dark); letter-spacing: 1px;
  }
  .tagline {
    position: absolute; right: 184px; top: 254px;
    font-size: 30px; font-weight: 200; color: var(--ink);
    letter-spacing: 1.5px; white-space: nowrap;
  }
  .modules {
    position: absolute; left: 250px; top: 340px; height: 56px;
    display: flex; align-items: center;
  }
  .module-icon { display: block; fill: var(--brand-blue); }
  .module-divider { width: 3px; height: 46px; background: var(--divider); margin: 0 22px; }

  /* Back */
  .person { position: absolute; left: 266px; top: 90px; }
  .person__name {
    font-size: 40px; font-weight: 700; color: var(--brand-blue);
    letter-spacing: -0.5px; line-height: 1; text-transform: uppercase;
    white-space: nowrap;
  }
  .person__role {
    margin: 8px 0 0 90px; font-size: 28px; font-weight: 400;
    color: var(--ink); line-height: 1;
  }
  .contact {
    position: absolute; left: 263px; display: flex; align-items: center;
  }
  .contact--address { top: 229px; }
  .contact--phone { top: 310px; }
  .contact--web { top: 389px; }
  .contact__badge {
    width: 42px; height: 42px; border-radius: 50%;
    background: var(--brand-blue); display: flex;
    align-items: center; justify-content: center; flex: none;
  }
  .contact__badge svg { fill: none; stroke: #fff; stroke-width: 1.6; }
  .contact__text {
    margin-left: 29px; font-size: 23px; font-weight: 400;
    color: var(--ink); line-height: 31px; white-space: nowrap;
  }
</style>
</head>
<body>
<main class="canvas">

  <section class="card card--front" aria-label="Card front">
    <div class="band band--l1"></div><div class="band band--l2"></div>
    <div class="band band--r1"></div><div class="band band--r2"></div>

    <div class="brand-dot" aria-hidden="true"></div>
    <h1 class="wordmark">flEnzo</h1>
    <p class="tagline">rewards that travel</p>

    <div class="modules" aria-label="Tours, cashback, takeaway, deals">
      <svg class="module-icon" width="66" height="52" viewBox="0 0 66 52" aria-label="Tours and activities">
        <path d="M6 10h14l5-8h16l5 8h14a6 6 0 0 1 6 6v30a6 6 0 0 1-6 6H6a6 6 0 0 1-6-6V16a6 6 0 0 1 6-6z"/>
        <circle cx="33" cy="30" r="13" fill="#fff"/><circle cx="33" cy="30" r="9.5"/>
        <circle cx="33" cy="30" r="7.5" fill="#fff"/>
        <circle cx="56" cy="18" r="2.5" fill="#fff"/>
      </svg>
      <div class="module-divider"></div>
      <svg class="module-icon" width="52" height="52" viewBox="0 0 52 52" aria-label="Cashback exchange">
        <path d="M4 14 L16 2 L16 9 C26 9 32 12 34 18 C30 15 24 15 16 16 L16 24 Z"/>
        <path d="M48 38 L36 50 L36 43 C26 43 20 40 18 34 C22 37 28 37 36 36 L36 28 Z"/>
        <circle cx="26" cy="26" r="11"/>
        <text x="26" y="32" font-size="16" font-weight="700" text-anchor="middle" fill="#fff" font-family="Source Sans 3, sans-serif">$</text>
      </svg>
      <div class="module-divider"></div>
      <svg class="module-icon" width="46" height="52" viewBox="0 0 46 52" aria-label="Takeaway ordering">
        <path d="M4 2v12a6 6 0 0 0 6 6l32 30 3-3L14 17a6 6 0 0 0 4-5V2h-2v10h-2V2h-2v10h-2V2h-2v10H7V2z"/>
        <ellipse cx="36" cy="10" rx="7" ry="9" transform="rotate(35 36 10)"/>
        <path d="M31 16 L1 47 l3 3 L34 20z"/>
      </svg>
      <div class="module-divider"></div>
      <svg class="module-icon" width="52" height="52" viewBox="0 0 52 52" aria-label="Local deals">
        <path d="M30 2h18a2 2 0 0 1 2 2v18L22 50 2 30z"/>
        <circle cx="40" cy="12" r="3.5" fill="#fff"/>
      </svg>
    </div>
  </section>

  <section class="card card--back" aria-label="Card back">
    <div class="band band--l1"></div><div class="band band--l2"></div>
    <div class="band band--r1"></div><div class="band band--r2"></div>

    <div class="person">
      <h2 class="person__name">Carla Whitfield</h2>
      <p class="person__role">marketing</p>
    </div>

    <div class="contact contact--address">
      <span class="contact__badge">
        <svg width="16" height="20" viewBox="0 0 16 20" aria-label="Address"><path d="M8 18s6-6.5 6-10.5a6 6 0 0 0-12 0C2 11.5 8 18 8 18z" fill="#fff" stroke="none"/><circle cx="8" cy="7.5" r="2" fill="#2e86cc" stroke="none"/></svg>
      </span>
      <p class="contact__text">Suite 7, Level 2, 14-18 Harrow Lane,<br>Sydney, NSW, 2000, Australia</p>
    </div>

    <div class="contact contact--phone">
      <span class="contact__badge">
        <svg width="14" height="22" viewBox="0 0 14 22" aria-label="Phone"><rect x="1.5" y="1" width="11" height="20" rx="2"/><line x1="1.5" y1="4" x2="12.5" y2="4"/><line x1="1.5" y1="17" x2="12.5" y2="17"/></svg>
      </span>
      <p class="contact__text">+ 61 407318265<br>+61 2 9375 4120</p>
    </div>

    <div class="contact contact--web">
      <span class="contact__badge">
        <svg width="20" height="20" viewBox="0 0 20 20" aria-label="Website"><circle cx="10" cy="10" r="8"/><ellipse cx="10" cy="10" rx="3.5" ry="8"/><line x1="2" y1="10" x2="18" y2="10"/><line x1="3.5" y1="6" x2="16.5" y2="6"/><line x1="3.5" y1="14" x2="16.5" y2="14"/></svg>
      </span>
      <p class="contact__text">W: www.flenzo.co</p>
    </div>
  </section>

</main>
</body>
</html>
```